Off Grid consulting and outdoor products needs a website

We need a website design to help launch our new business. Its a business that plans to offer Off-grid conslting and outdoor survival products to people who are looking to relocate or vacation to properties/homes that are Off-grid. We plan to offer design plans for homes/cabins, renewable energy systems for power/heating etc, survival products for outdoor vacations/living. We also do consulting and project management for those who want to design and build from scratch their dream off-grid home or vacation property. I've included our logo design for use.
Would like the website to include 5 pages.
www.bramblequietlands.com
The main landing page (1)
want a video loop backround with a flyover of a cabin in the woods.
https://www.clipvaultmedia.com/video/clip-48213307-pale-sky-thawing-frost-on-pine-slope
(also need a backup static image of just high-shot of cabin in woods)
logo top left, Quoted string of text in the middle, over the video. and a CTA button to 'Contact us'
picture links below that to last 3 recent blog posts.
About Us page (2)
(example) https://larkhollowgear.com/pages/about-lark
Blog page (3)
blog posts associated with pictures.
Consulting 'services' page (4)
-land services and moving off-grid
-Building off grid
-Renewable energy off-grid
-Sustainable farming and all season greenhouses
Store page 'comming soon' (5)
(Example) http://hearthkeep.quillstheme.com/demo-1/demo.html

Target Market(s)

Outdoor enthusiasts and people who want to escape their city life

Coding

Coded - Design and coding required

Requirements
Must have
• Outdoor feel, woods, cabin, reneable energy (solar, geothermal, greenhouses, water wells)

```html
<!DOCTYPE html>
<html lang="en">
<head>
<meta charset="utf-8">
<title>Bramble Quietlands</title>
<link rel="stylesheet" href="https://fonts.googleapis.com/css2?family=Oswald:wght@400;500;600&family=Poppins:wght@400;500;600;700&display=swap">
<style>
:root{
  --rust:#a0461a;
  --tan:#cf9a76;
  --cream:#fcefe1;
  --footer-bg:#fdf7f2;
  --ink:#1d1d1d;
  --muted:#6b6b6b;
  --teal:#1f6f86;
  --violet:#8a6bb8;
  --white:#ffffff;
}
*{margin:0;padding:0;box-sizing:border-box}
html,body{width:1200px;height:2345px;overflow:hidden;background:var(--white)}
body{position:relative;font-family:"Poppins",sans-serif;color:var(--ink)}

/* Hero */
.hero{position:absolute;left:0;top:0;width:1200px;height:508px;
  background:linear-gradient(180deg,#3c3e42 0%,#4a4c4f 25%,#35373a 55%,#24272a 100%)}
.hero-photo{position:absolute;inset:0;
  background:radial-gradient(ellipse at 50% 90%,#55585b 0%,rgba(40,42,45,0) 45%),
             linear-gradient(180deg,rgba(90,92,96,.35) 0%,rgba(30,32,34,.2) 60%,rgba(20,22,24,.5) 100%)}
.brand{position:absolute;left:87px;top:44px;display:flex;align-items:center;gap:10px;
  font-family:"Oswald",sans-serif;font-weight:600;font-size:30px;line-height:1;color:var(--white);text-transform:uppercase}
.brand-mark{width:22px;height:22px;border-radius:50%;background:var(--white)}
.nav{position:absolute;left:455px;top:45px;display:flex;font-family:"Oswald",sans-serif;font-size:17px}
.nav a{color:var(--white);text-decoration:none;padding:0 11px 6px;margin-right:15px}
.nav a.active{color:var(--tan);border-bottom:2px solid var(--tan)}
.call{position:absolute;left:959px;top:40px;display:flex;align-items:center;gap:9px;font-family:"Oswald",sans-serif}
.call-icon{width:34px;height:34px;border-radius:50%;background:var(--tan);display:flex;align-items:center;justify-content:center}
.call small{display:block;font-size:10px;color:var(--tan)}
.call strong{display:block;font-size:19px;font-weight:500;color:var(--white);line-height:1.1}
.hero-title{position:absolute;left:0;width:1200px;top:212px;text-align:center;font-family:"Oswald",sans-serif;
  font-weight:500;font-size:39px;line-height:45px;color:var(--tan)}

/* Buttons */
.btn{position:absolute;height:39px;display:flex;align-items:center;justify-content:center;
  font-family:"Oswald",sans-serif;font-size:19px;text-decoration:none}
.btn::after{content:"";position:absolute;left:5px;top:5px;right:-5px;bottom:-5px;border:1px solid var(--tan);z-index:-1}
.btn-solid{background:var(--tan);color:var(--white)}
.btn-outline{background:var(--white);color:var(--ink);border:2px solid var(--ink)}
.btn-wrap{position:absolute;z-index:1}

/* Section titles */
.section-title{position:absolute;left:0;width:1200px;text-align:center;font-family:"Oswald",sans-serif;
  font-weight:600;font-size:38px;color:var(--rust);line-height:1}
.section-title span{position:relative;padding:0 20px}
.section-title span::before,.section-title span::after{content:"";position:absolute;top:50%;width:45px;height:1px;background:var(--rust)}
.section-title span::before{right:100%}
.section-title span::after{left:100%}

.about-text{position:absolute;left:156px;width:888px;top:644px;text-align:center;font-size:14px;line-height:24px;color:var(--ink)}

/* Services */
.services{position:absolute;left:0;top:911px;width:1200px;height:489px;background:var(--cream)}
.service{position:absolute;top:158px;width:238px;height:260px}
.service-photo{position:absolute;left:0;top:0;width:238px;height:236px}
.service-label{position:absolute;left:0;top:197px;width:203px;height:62px;background:var(--white);
  display:flex;align-items:center;padding:0 14px 0 16px;font-weight:600;font-size:14px;line-height:19px;border-right:4px solid}
.service-label.compact{width:166px;border-right:0;padding:0 8px 0 14px;font-size:13.5px;line-height:17px}
.service-next{position:absolute;left:166px;top:197px;width:37px;height:62px;background:var(--tan);display:flex;align-items:center;justify-content:center}

/* Blogs */
.blog{position:absolute;top:1558px;width:325px}
.blog-photo{width:325px;height:211px}
.blog-card{position:absolute;left:13px;width:300px;background:var(--white);box-shadow:0 4px 16px rgba(0,0,0,.08);
  padding:18px 14px 24px 16px;display:flex;gap:12px}
.blog-date{width:50px;flex:none;text-align:center}
.blog-date b{display:block;font-size:29px;font-weight:700;color:var(--rust);line-height:1}
.blog-date small{font-size:11px;color:var(--muted)}
.blog-body p{font-size:12.5px;line-height:20px;color:var(--ink)}
.blog-more{display:inline-block;margin-top:18px;width:111px;height:28px;line-height:26px;text-align:center;font-size:11px;
  border:1px solid var(--tan);color:var(--rust);text-decoration:none}
.blog-more.filled{background:var(--tan);color:var(--white)}

/* Footer */
.footer{position:absolute;left:0;top:2094px;width:1200px;height:208px;background:var(--footer-bg)}
.contact-item{position:absolute;top:70px;display:flex;align-items:center;gap:13px}
.contact-icon{width:48px;height:48px;border-radius:50%;background:var(--rust);display:flex;align-items:center;justify-content:center}
.contact-item small{display:block;font-size:12.5px;color:var(--ink)}
.contact-item strong{display:block;font-family:"Oswald",sans-serif;font-weight:400;font-size:15px;color:var(--rust)}
.footer-nav{position:absolute;left:370px;top:142px;display:flex;font-family:"Oswald",sans-serif;font-size:17px}
.footer-nav a{color:var(--ink);text-decoration:none;padding:0 17px 6px;margin-right:9px}
.footer-nav a.active{color:var(--rust);border-bottom:3px solid var(--rust)}
.bottom-bar{position:absolute;left:0;top:2302px;width:1200px;height:43px;background:var(--rust);color:var(--white)}
.bottom-bar p{position:absolute;left:87px;top:12px;font-size:13px}
.socials{position:absolute;right:87px;top:11px;display:flex;gap:15px}
.socials span{width:21px;height:21px;border-radius:50%;background:rgba(255,255,255,.55)}
.socials span.on{background:var(--white)}
</style>
</head>
<body>

<header class="hero">
  <div class="hero-photo" role="img" aria-label="Aerial view over snowy pine forest and mountains toward a cabin roof with solar panels"></div>
  <div class="brand"><span class="brand-mark"></span>Bramble Quietlands</div>
  <nav class="nav">
    <a class="active" href="#">Home</a><a href="#">About Us</a><a href="#">Blogs</a><a href="#">Services</a><a href="#">Contact Us</a>
  </nav>
  <div class="call">
    <div class="call-icon"><svg width="16" height="16" viewBox="0 0 24 24"><path fill="#fff" d="M6.6 10.8a15 15 0 0 0 6.6 6.6l2.2-2.2a1 1 0 0 1 1-.25 11.4 11.4 0 0 0 3.6.57 1 1 0 0 1 1 1V20a1 1 0 0 1-1 1A17 17 0 0 1 3 4a1 1 0 0 1 1-1h3.5a1 1 0 0 1 1 1c0 1.25.2 2.45.57 3.57a1 1 0 0 1-.25 1z"/></svg></div>
    <div><small>Call Us</small><strong>800-555-0147</strong></div>
  </div>
  <h1 class="hero-title">Lorem Ipsum is simply dummy text<br>of the printing industry.</h1>
  <div class="btn-wrap" style="left:523px;top:328px"><a class="btn btn-solid" style="position:relative;width:150px" href="#">Contact Us</a></div>
</header>

<h2 class="section-title" style="top:584px"><span>About Us</span></h2>
<p class="about-text">Lorem Ipsum is simply dummy text of the printing and typesetting industry. Lorem Ipsum has been the industry's standard dummy text ever since the 1500s, when an unknown printer took a galley of type and scrambled it to make a type specimen book. It has survived not only five centuries, but also the leap into electronic typesetting, remaining essentially unchanged. It was popularised in the 1960s with the release of Tarnwick sheets containing Lorem Ipsum passages, and more recently with desktop publishing software like Quillset Layout including versions of Lorem Ipsum.</p>
<div class="btn-wrap" style="left:522px;top:789px"><a class="btn btn-outline" style="position:relative;width:150px" href="#">Contact Us</a></div>

<section class="services">
  <h2 class="section-title" style="top:77px"><span>Our Services</span></h2>
  <div class="service" style="left:87px">
    <div class="service-photo" role="img" aria-label="Timber cabin frame under construction in the desert" style="background:linear-gradient(180deg,#8fb3d9 0%,#b9cde0 45%,#a98a66 70%,#5e5348 100%)"></div>
    <div class="service-label" style="color:var(--rust);border-color:var(--rust)">Land Services and Moving off Grid</div>
  </div>
  <div class="service" style="left:350px">
    <div class="service-photo" role="img" aria-label="Orange wooden cabin by a lake in the pine forest" style="background:linear-gradient(180deg,#9a8f5a 0%,#7c6a3c 35%,#c57a2a 55%,#3d3a22 100%)"></div>
    <div class="service-label" style="color:var(--teal);border-color:var(--teal)">Building off Grid</div>
  </div>
  <div class="service" style="left:612px">
    <div class="service-photo" role="img" aria-label="Field of solar panels seen from above" style="background:linear-gradient(160deg,#6b6a44 0%,#8a8c86 40%,#9aa2a6 60%,#7a6848 100%)"></div>
    <div class="service-label" style="color:var(--violet);border-color:var(--violet)">Renewable Energy off Grid</div>
  </div>
  <div class="service" style="left:874px">
    <div class="service-photo" role="img" aria-label="Small hut on green terraced farmland in the hills" style="background:linear-gradient(180deg,#9bb7cf 0%,#a8bcc6 35%,#7f9b5a 60%,#b7a13a 100%)"></div>
    <div class="service-label compact" style="color:var(--rust)">Sustainable farm&shy;ing and all season green houses</div>
    <div class="service-next"><svg width="10" height="14" viewBox="0 0 10 14"><path d="M2 1l6 6-6 6" fill="none" stroke="#fff" stroke-width="2"/></svg></div>
  </div>
</section>

<h2 class="section-title" style="top:1477px"><span>Blogs</span></h2>

<article class="blog" style="left:87px">
  <div class="blog-photo" role="img" aria-label="Glass-fronted cabin among tall forest trees" style="background:linear-gradient(180deg,#8fa5b8 0%,#6f7a4c 45%,#3f4a34 75%,#6b7a3e 100%)"></div>
  <div class="blog-card" style="top:204px">
    <div class="blog-date"><b>18</b><small>Apr, 22</small></div>
    <div class="blog-body"><p>Lorem Ipsum is simply dummy text of the printing and typeset&shy;ting industry. Lorem Ipsum has been the industry's...</p><a class="blog-more" href="#">Explore More</a></div>
  </div>
</article>
<article class="blog" style="left:437px">
  <div class="blog-photo" role="img" aria-label="Solar panels on a dark cabin roof under blue sky" style="background:linear-gradient(180deg,#b7cde8 0%,#9db4cf 25%,#2f3a5a 45%,#3c4a62 70%,#6d8a4c 100%)"></div>
  <div class="blog-card" style="top:204px">
    <div class="blog-date"><b>25</b><small>Apr, 22</small></div>
    <div class="blog-body"><p>Lorem Ipsum is simply dummy text of the printing and typeset&shy;ting industry. Lorem Ipsum has been the industry's...</p><a class="blog-more" href="#">Explore More</a></div>
  </div>
</article>
<article class="blog" style="left:787px">
  <div class="blog-photo" role="img" aria-label="House shape made of green grass in sunny meadow" style="background:radial-gradient(circle at 30% 30%,#f4f1b0 0%,#b8cf5a 35%,#5c8a2a 100%)"></div>
  <div class="blog-card" style="top:140px">
    <div class="blog-date"><b>28</b><small>Apr, 22</small></div>
    <div class="blog-body"><p>Lorem Ipsum is simply dummy text of the printing and typeset&shy;ting industry. Lorem Ipsum has been the industry's...</p><a class="blog-more filled" href="#">Explore More</a></div>
  </div>
</article>

<div class="btn-wrap" style="left:523px;top:1973px"><a class="btn btn-outline" style="position:relative;width:150px" href="#">View All</a></div>

<footer class="footer">
  <div class="contact-item" style="left:201px">
    <div class="contact-icon"><svg width="18" height="22" viewBox="0 0 18 22"><path fill="#fff" d="M9 0a8 8 0 0 0-8 8c0 6 8 14 8 14s8-8 8-14a8 8 0 0 0-8-8zm0 11a3 3 0 1 1 0-6 3 3 0 0 1 0 6z"/></svg></div>
    <div><small>Address</small><strong>PO Box 418 . Kerrowdale . Northvale</strong></div>
  </div>
  <div class="contact-item" style="left:526px">
    <div class="contact-icon"><svg width="20" height="20" viewBox="0 0 24 24"><path fill="#fff" d="M6.6 10.8a15 15 0 0 0 6.6 6.6l2.2-2.2a1 1 0 0 1 1-.25 11.4 11.4 0 0 0 3.6.57 1 1 0 0 1 1 1V20a1 1 0 0 1-1 1A17 17 0 0 1 3 4a1 1 0 0 1 1-1h3.5a1 1 0 0 1 1 1c0 1.25.2 2.45.57 3.57a1 1 0 0 1-.25 1z"/></svg></div>
    <div><small>Call</small><strong>+64 9 555 0182</strong></div>
  </div>
  <div class="contact-item" style="left:766px">
    <div class="contact-icon"><svg width="22" height="16" viewBox="0 0 22 16"><rect x="1" y="1" width="20" height="14" fill="none" stroke="#fff" stroke-width="2"/><path d="M1 1l10 8 10-8" fill="none" stroke="#fff" stroke-width="2"/></svg></div>
    <div><small>Email</small><strong>info@bramblequietlands.com</strong></div>
  </div>
  <nav class="footer-nav">
    <a class="active" href="#">Home</a><a href="#">About Us</a><a href="#">Blogs</a><a href="#">Services</a><a href="#">Contact Us</a>
  </nav>
</footer>

<div class="bottom-bar">
  <p>Copyright © 2022 Bramble Quietlands. All Rights Reserved</p>
  <div class="socials"><span></span><span></span><span class="on"></span><span></span></div>
</div>

</body>
</html>
```